Modern, Sleek Business Card Design for Corvane Systems

Please create a modern business card, preferably all black with white logo and writing for Corvane Systems, a defense and aerospace company.

Contact Information for Business Card

symbol on one side and name, title, contact info on the other side.

```html
<!DOCTYPE html>
<html lang="en">
<head>
<meta charset="utf-8">
<title>Corvane Systems – Business Card</title>
<link rel="stylesheet" href="https://fonts.googleapis.com/css2?family=Montserrat:wght@500;700&family=Arimo:wght@400&display=swap">
<style>
  :root {
    --stage: #3b3b3b;
    --card: #1f1f1f;
    --card-edge: #262626;
    --gloss: #3a3a3a;
    --ink: #ffffff;
    --ink-soft: #e6e6e6;
  }
  * { margin: 0; padding: 0; box-sizing: border-box; }
  html, body { width: 1200px; height: 875px; overflow: hidden; background: var(--stage); }
  .stage { position: relative; width: 1200px; height: 875px; }
  .card {
    position: absolute;
    width: 520px; height: 300px;
    background: var(--card);
    border: 1px solid var(--card-edge);
    border-radius: 22px;
    box-shadow: 0 18px 40px rgba(0,0,0,.45);
  }
  .card--front { left: 80px; top: 130px; display: flex; align-items: center; justify-content: center; }
  .card--back { left: 600px; top: 440px; padding: 40px 44px; }

  .wordmark {
    font-family: "Montserrat", sans-serif;
    font-weight: 500;
    letter-spacing: 6px;
    text-transform: uppercase;
    display: flex; align-items: center; gap: 14px;
  }
  .wordmark__mark { width: 14px; height: 14px; }
  .card--front .wordmark { font-size: 30px; color: var(--gloss); }
  .card--front .wordmark__mark { background: var(--gloss); }
  .card--back .wordmark { font-size: 22px; color: var(--ink); letter-spacing: 4px; }
  .card--back .wordmark__mark { background: var(--ink); width: 11px; height: 11px; }

  .holder { margin-top: 30px; }
  .holder__name {
    font-family: "Montserrat", sans-serif; font-weight: 700;
    font-size: 22px; color: var(--ink); letter-spacing: 1px; text-transform: uppercase;
  }
  .holder__title { font-family: "Arimo", sans-serif; font-size: 14px; color: var(--ink-soft); margin-top: 2px; }

  .address { font-family: "Arimo", sans-serif; font-size: 14px; line-height: 1.3; color: var(--ink-soft); margin-top: 16px; }

  .contacts { list-style: none; margin-top: 14px; font-family: "Arimo", sans-serif; font-size: 14px; color: var(--ink-soft); }
  .contacts li { display: flex; align-items: center; gap: 9px; line-height: 1.5; }
  .contacts svg { width: 12px; height: 12px; fill: none; stroke: var(--ink); stroke-width: 1.6; }
</style>
</head>
<body>
<main class="stage">
  <section class="card card--front" aria-label="Card front">
    <div class="wordmark"><span class="wordmark__mark"></span>Corvane Systems</div>
  </section>

  <section class="card card--back" aria-label="Card back">
    <div class="wordmark"><span class="wordmark__mark"></span>Corvane Systems</div>
    <div class="holder">
      <h1 class="holder__name">Daniel Mercer</h1>
      <p class="holder__title">CEO/Founder</p>
    </div>
    <p class="address">P.O Box 4170 Harbor Street<br>Lakeview ON 40417</p>
    <ul class="contacts">
      <li>
        <svg viewBox="0 0 12 12" aria-hidden="true"><path d="M2 1.5 L4 1.5 L5 4 L3.8 5 Q5 7.2 7 8.2 L8 7 L10.5 8 L10.5 10 Q6 10.5 3.5 8 Q1.5 5.5 2 1.5 Z"/></svg>
        +52-55-3104-2278
      </li>
      <li>
        <svg viewBox="0 0 12 12" aria-hidden="true"><rect x="1" y="2.5" width="10" height="7"/><path d="M1 2.5 L6 6.5 L11 2.5"/></svg>
        info@corvanesystems.com
      </li>
      <li>
        <svg viewBox="0 0 12 12" aria-hidden="true"><circle cx="6" cy="6" r="4.8"/><path d="M1.2 6 H10.8 M6 1.2 Q3 6 6 10.8 M6 1.2 Q9 6 6 10.8"/></svg>
        www.corvanesystems.com
      </li>
    </ul>
  </section>
</main>
</body>
</html>
```